Bref créative
Business Card and Stationary Project
for an Energy Healing business
I need double sided standard sized Business Card [3.5" x 2"]
Please see the uploaded .doc file for examples of the fonts I like and other info.
Modern
Lena Brackwood
#314 - 5862 Fenlow Avenue
Port Coquitlam, B.C.
BrightmereGroveHealing@example.net
Please DO NOT put any personal information on the front of the card. I had to fill in those sections but that's not what I want. I want the logo - as big as possible and in the middle - on the front of the card except for the words (in the upper, right corner of the card) to say "Take Back Your Life!". I want a medium blue background color on the front of the card. Likely one of the logo files I uploaded will show an example of this. Please see the .doc file I uploaded for examples of the words (font) and a (medium) blue I like, though I also like the medium blue in the logo example.
I have no preconceived ideas for the stationary, other than I would like it to be relatively low cost to print please.
The back of the card will have a light blue background color and all of my personal information centered please. Again, please see the .doc file I uploaded for the light blue I want for the background color of the back of the card and for examples of the fonts I like for the information.
Remover of Obstacles and Goddess of New Beginnings
Email: BrightmereGroveHealing@example.net
Phone: (604) 555-3187
Website: BrightmereGroveHealing.example

```html
<!DOCTYPE html>
<html lang="en">
<head>
<meta charset="utf-8">
<title>Brightmere Grove – Stationery Option 1</title>
<link rel="stylesheet" href="https://fonts.googleapis.com/css2?family=Didact+Gothic&family=Questrial&display=swap">
<style>
  :root {
    --backdrop: #e9e5df;
    --paper: #ffffff;
    --paper-edge: #d9d6d0;
    --leaf-green: #8cc43f;
    --ink-grey: #8a8a8a;
    --label-ink: #4a4640;
    --navy-card: #2c3c8e;
    --sky-card: #2f9bd7;
    --cornflower-card: #5f92da;
    --mist-card: #6fa2e2;
    --white: #ffffff;
    --bird-wash: rgba(140, 196, 63, 0.07);
  }
  * { box-sizing: border-box; margin: 0; padding: 0; }
  html, body { width: 1200px; height: 700px; overflow: hidden; }
  body { background: var(--backdrop); font-family: "Didact Gothic", "Questrial", sans-serif; position: relative; }

  .sheet { position: absolute; background: var(--paper); box-shadow: 0 2px 6px rgba(0,0,0,0.25); }

  .brand-name { font-family: "Questrial", sans-serif; font-weight: 400; color: var(--leaf-green); white-space: nowrap; }
  .brand-tagline { font-family: "Questrial", sans-serif; color: var(--ink-grey); white-space: nowrap; }

  /* Letterhead */
  .letterhead { left: 36px; top: 19px; width: 444px; height: 610px; }
  .letterhead .brand { position: absolute; top: 22px; left: 0; right: 0; text-align: center; }
  .letterhead .brand-name { font-size: 30px; }
  .letterhead .brand-tagline { font-size: 8px; margin-top: 2px; }
  .letterhead .watermark { position: absolute; left: 40px; top: 150px; width: 340px; height: 340px; }
  .letterhead-footer { position: absolute; bottom: 34px; left: 0; right: 0; text-align: center; font-size: 7px; color: var(--ink-grey); }
  .letterhead-contacts { position: absolute; bottom: 14px; left: 30px; right: 30px; display: flex; justify-content: space-between; font-size: 6.5px; color: var(--ink-grey); }
  .letterhead-contacts b { color: var(--leaf-green); font-weight: 400; }
  .sheet-label { position: absolute; font-size: 11px; color: var(--label-ink); text-align: center; }

  /* Envelopes */
  .envelope-back { left: 533px; top: 19px; width: 626px; height: 128px; }
  .envelope-back .flap { position: absolute; inset: 0; }
  .envelope-back .brand { position: absolute; top: 10px; left: 0; right: 0; text-align: center; }
  .envelope-back .brand-name { font-size: 22px; }
  .envelope-back .brand-tagline { font-size: 6px; }
  .envelope-front { left: 540px; top: 120px; width: 580px; height: 196px; }
  .envelope-front .brand { position: absolute; top: 22px; left: 24px; text-align: center; }
  .envelope-front .brand-name { font-size: 24px; }
  .envelope-front .brand-tagline { font-size: 6.5px; }
  .envelope-front .return-address { position: absolute; top: 84px; left: 24px; font-size: 6.5px; color: var(--ink-grey); }

  /* Business cards */
  .card { position: absolute; width: 206px; height: 118px; box-shadow: 0 2px 5px rgba(0,0,0,0.3); color: var(--white); overflow: hidden; }
  .card-front { background: var(--navy-card); }
  .card-front .slogan { position: absolute; top: 8px; right: 10px; font-size: 7.5px; }
  .card-front .brand { position: absolute; top: 40px; left: 0; right: 0; text-align: center; }
  .card-front .brand-name { font-size: 24px; }
  .card-front .brand-tagline { font-size: 6px; color: #c9d3f0; }

  .card-back { text-align: center; padding-top: 14px; }
  .card-back .holder-name { font-size: 14px; font-weight: 700; letter-spacing: 0.2px; }
  .card-back .holder-role { font-size: 5.5px; margin-top: 2px; }
  .card-back .contact-list { list-style: none; margin-top: 14px; font-size: 6.5px; line-height: 1.5; text-align: left; display: inline-block; }
  .card-back .contact-list b { font-weight: 700; }
  .card-back.layout-left { text-align: left; padding-left: 14px; padding-top: 14px; }
  .back-sky { background: var(--sky-card); }
  .back-cornflower { background: var(--cornflower-card); }
  .back-mist { background: var(--mist-card); }

  .card-label { position: absolute; width: 206px; text-align: center; font-size: 7px; color: var(--label-ink); }
</style>
</head>
<body>

  <!-- Letterhead -->
  <section class="sheet letterhead">
    <div class="brand">
      <div class="brand-name">Brightmere Grove</div>
      <div class="brand-tagline">Energy Healing</div>
    </div>
    <svg class="watermark" viewBox="0 0 340 340" role="img" aria-label="Faint large brand symbol area">
      <circle cx="170" cy="170" r="165" fill="var(--bird-wash)"/>
    </svg>
    <div class="letterhead-footer">#314 - 5862 Fenlow Avenue, Port Coquitlam, B.C. V3B 2K7</div>
    <div class="letterhead-contacts">
      <span><b>E:</b> BrightmereGroveHealing@example.net</span>
      <span><b>P:</b> (604) 555-3187</span>
      <span><b>W:</b> BrightmereGroveHealing.example</span>
    </div>
  </section>
  <div class="sheet-label" style="left:36px; top:638px; width:444px;">Option 1</div>

  <!-- Envelope back -->
  <section class="sheet envelope-back">
    <svg class="flap" viewBox="0 0 626 128" preserveAspectRatio="none" aria-hidden="true">
      <polyline points="0,70 313,122 626,70" fill="none" stroke="var(--paper-edge)" stroke-width="1"/>
    </svg>
    <div class="brand">
      <div class="brand-name">Brightmere Grove</div>
      <div class="brand-tagline">Energy Healing</div>
    </div>
  </section>

  <!-- Envelope front -->
  <section class="sheet envelope-front">
    <div class="brand">
      <div class="brand-name">Brightmere Grove</div>
      <div class="brand-tagline">Energy Healing</div>
    </div>
    <div class="return-address">#314 - 5862 Fenlow Avenue, Port Coquitlam, B.C. V3B 2K7</div>
  </section>

  <!-- Business card front -->
  <article class="card card-front" style="left:533px; top:372px;">
    <div class="slogan">Take Back Your Life!</div>
    <div class="brand">
      <div class="brand-name">Brightmere Grove</div>
      <div class="brand-tagline">Energy Healing</div>
    </div>
  </article>
  <div class="card-label" style="left:533px; top:496px;">BC Card</div>

  <!-- Card backs -->
  <article class="card card-back back-sky" style="left:749px; top:372px;">
    <div class="holder-name">Lena Brackwood</div>
    <div class="holder-role">Remover of Obstacles and Goddess of New Beginnings</div>
    <ul class="contact-list">
      <li><b>Email:</b> BrightmereGroveHealing@example.net</li>
      <li><b>Phone:</b> (604) 555-3187</li>
      <li><b>Website:</b> BrightmereGroveHealing.example</li>
    </ul>
  </article>
  <div class="card-label" style="left:749px; top:496px;">BC Back 1</div>

  <article class="card card-back back-cornflower" style="left:960px; top:372px;">
    <div class="holder-name">Lena Brackwood</div>
    <div class="holder-role">Remover of Obstacles and Goddess of New Beginnings</div>
    <ul class="contact-list">
      <li><b>Email:</b> BrightmereGroveHealing@example.net</li>
      <li><b>Phone:</b> (604) 555-3187</li>
      <li><b>Website:</b> BrightmereGroveHealing.example</li>
    </ul>
  </article>
  <div class="card-label" style="left:960px; top:496px;">BC Back 2</div>

  <article class="card card-back layout-left back-mist" style="left:665px; top:552px;">
    <div class="holder-name">Lena Brackwood</div>
    <div class="holder-role">Remover of Obstacles and Goddess of New Beginnings</div>
    <ul class="contact-list">
      <li><b>Email:</b> BrightmereGroveHealing@example.net</li>
      <li><b>Phone:</b> (604) 555-3187</li>
      <li><b>Website:</b> BrightmereGroveHealing.example</li>
    </ul>
  </article>
  <div class="card-label" style="left:665px; top:676px;">BC Back 3</div>

  <article class="card card-back layout-left back-sky" style="left:876px; top:552px;">
    <div class="holder-name">Lena Brackwood</div>
    <div class="holder-role">Remover of Obstacles and Goddess of New Beginnings</div>
    <ul class="contact-list">
      <li><b>Email:</b> BrightmereGroveHealing@example.net</li>
      <li><b>Phone:</b> (604) 555-3187</li>
      <li><b>Website:</b> BrightmereGroveHealing.example</li>
    </ul>
  </article>
  <div class="card-label" style="left:876px; top:676px;">BC Back 4</div>

</body>
</html>
```